Redesign Website

I currently have a website www.quillbrookrehab.com that I would like to have redesigned for esthetics and design limitations with the present platform. I will provide my logo, background logo (attached) , current site, foundation grip PSD.zip (attached) and a questionnaire (attached) from a web design company to provide the input to have an impressive site that pleases the eyes and makes an impact. I would also like the site to be mobile friendly.

IMPORTANT:
- The final PSD must include:
o Homepage Mockup
o Internal Pages Mockup
o Mobile site mockup
o Fonts files used in mockup

Final website will be responsive, using the Foundation Framework. Attached you will find a PSD of the Foundation grid – please use this and include with your final PSD. Here is a link for reference:
http://plenvix.com/article/1053/foundation-s-grid-and-photoshop-what-you-

Target Market(s)

Patients for physical therapy

Industry/Entity Type

It Company

Requirements
Must have
• Pages included in the present site. Photos and design should change.
Nice to have
• Should provide information necessary for patients to schedule an appointment
Should not have
• Should not be difficult to read.

```html
<!DOCTYPE html>
<html lang="en">
<head>
<meta charset="utf-8">
<title>Quillbrook Sports &amp; Orthopedic Physical Therapy</title>
<link rel="stylesheet" href="https://fonts.googleapis.com/css2?family=Roboto:wght@300;400;500&family=Roboto+Slab:wght@300;400&display=swap">
<style>
:root{
  --orange:#e8641e;
  --gold:#f0a31c;
  --ink:#333333;
  --muted:#555555;
  --line:#e2e2e2;
  --paper:#ffffff;
  --sand:#f4f1ee;
}
*{margin:0;padding:0;box-sizing:border-box}
html,body{width:795px;height:1200px;overflow:hidden;background:var(--paper)}
body{position:relative;font-family:"Roboto",Arial,sans-serif;color:var(--ink)}
.abs{position:absolute}

/* header */
.topbar{left:0;top:0;width:795px;height:38px;background:var(--paper);border-bottom:1px solid var(--line)}
.navbar{left:0;top:38px;width:795px;height:28px;background:#f7f7f7}
.btn-appointment{left:616px;top:10px;width:66px;height:20px;background:var(--gold);color:#fff;font:400 9px "Roboto",sans-serif;display:flex;align-items:center;justify-content:center;border:1px solid #d98e0c}
.brand{left:111px;top:0;width:99px;height:103px;background:var(--paper);box-shadow:0 1px 4px rgba(0,0,0,.25);z-index:3;display:flex;flex-direction:column;align-items:center;justify-content:center;gap:6px;padding:0 6px;text-align:center}
.brand-dot{width:22px;height:22px;border-radius:50%;background:var(--orange)}
.brand-name{font:400 10px/1.2 "Roboto Slab",serif;color:var(--orange)}
.main-nav{left:227px;top:44px;display:flex;gap:15px;font:400 9.5px "Roboto Slab",serif;color:#444}

/* hero */
.hero{left:0;top:66px;width:795px;height:280px;background:linear-gradient(100deg,#cfc7bd 0%,#b8ab9e 35%,#9a8f86 60%,#c9c2ba 100%)}
.hero-banner{left:466px;top:154px;width:329px;height:81px;background:rgba(240,163,28,.85);padding:12px 0 0 24px;color:#fff}
.hero-title{font:500 31px/1 "Roboto",sans-serif;letter-spacing:.5px}
.hero-sub{font:300 17px/1.3 "Roboto Slab",serif;margin-top:3px}

/* contact strip */
.strip{left:0;top:346px;width:795px;height:75px;background:var(--paper);border-bottom:1px solid var(--line)}
.strip-lead{left:113px;top:366px;color:var(--orange);font:400 11px/1.3 "Roboto Slab",serif}
.strip-lead b{display:block;font-weight:400;font-size:15px}
.chevron{left:212px;top:346px}
.icon{width:25px;height:25px;border-radius:50%;background:var(--orange);display:flex;align-items:center;justify-content:center;flex:none}
.strip-item{display:flex;align-items:center;gap:9px}
.strip-call{left:252px;top:367px}
.strip-place{left:408px;top:362px}
.strip-form{left:570px;top:367px}
.strip-accent{font:400 14px/1.2 "Roboto Slab",serif;color:var(--orange)}
.strip-small{font:400 10.5px/1.35 "Roboto Slab",serif;color:var(--ink)}

/* bio */
.bio{left:0;top:421px;width:795px;height:369px;background:radial-gradient(ellipse at 40% 45%,#fafafa 0%,#ececec 60%,#dedede 100%)}
.bio-name{left:110px;top:476px;font:400 20px "Roboto",sans-serif;color:#333}
.bio-text{left:112px;top:520px;width:425px;font:300 9.2px/15.4px "Roboto",sans-serif;color:var(--muted)}
.bio-photo{left:552px;top:514px;width:243px;height:276px;background:linear-gradient(180deg,#d9c3b2 0%,#cfb6a4 45%,#8fb0d6 75%,#7da3cf 100%);border-radius:120px 120px 0 0}

/* services */
.services-title{left:112px;top:811px;font:400 16px "Roboto",sans-serif;color:#333}
.svc-list{list-style:none;font:300 8.8px/16px "Roboto",sans-serif;color:var(--muted);white-space:nowrap}
.svc-list li{padding-left:8px;position:relative}
.svc-list li::before{content:"";position:absolute;left:0;top:6px;border-left:4px solid #aaa;border-top:2.5px solid transparent;border-bottom:2.5px solid transparent}
.svc-list .gap{margin-top:16px}
.svc-photo{left:668px;top:816px;width:127px;height:161px;background:linear-gradient(160deg,#fff 0%,#f2c9a5 35%,#f08b4d 60%,#c7b7a6 100%)}

/* testimonials */
.testimonials{left:0;top:977px;width:795px;height:168px;background:var(--sand)}
.testi-title{left:112px;top:1003px;font:400 16px "Roboto",sans-serif;color:#333}
.testi-text{left:113px;top:1036px;width:475px;font:300 9px/16px "Roboto",sans-serif;color:var(--muted)}
.testi-rule{left:602px;top:1036px;width:1px;height:78px;background:#d8d2cc}
.avatar{left:623px;top:1038px;width:53px;height:53px;border-radius:50%;border:2px solid #fff;background:linear-gradient(#f3c79b,#e89a5a)}
.testi-who{left:622px;top:1098px;font:400 9px "Roboto",sans-serif;color:#555}
.testi-who b{font-weight:500}

/* footer */
.footer{left:0;top:1145px;width:795px;height:55px;background:var(--paper);border-top:1px solid var(--line)}
.copyright{left:111px;top:1166px;font:300 9px "Roboto",sans-serif;color:#555}
.social{width:25px;height:25px;border-radius:50%;background:var(--orange);top:1160px}
</style>
</head>
<body>

<header>
  <div class="abs topbar"></div>
  <div class="abs navbar"></div>
  <a class="abs btn-appointment">Appointment!</a>
  <div class="abs brand">
    <span class="brand-dot"></span>
    <span class="brand-name">Quillbrook Sports &amp; Orthopedic Physical Therapy</span>
  </div>
  <nav class="abs main-nav">
    <span>About us</span><span>Hours</span><span>Our Story</span><span>Services</span><span>Insurance</span><span>New Patients</span><span>Contact Us</span><span>Community</span>
  </nav>
</header>

<section>
  <div class="abs hero" role="img" aria-label="Photo of a therapist stretching a patient's leg on a treatment table in a clinic gym"></div>
  <div class="abs hero-banner">
    <div class="hero-title">EXPERIENCE</div>
    <div class="hero-sub">you can trust!</div>
  </div>
</section>

<section>
  <div class="abs strip"></div>
  <div class="abs strip-lead">Schedule Your<b>Appointment!</b></div>
  <svg class="abs chevron" width="18" height="75" viewBox="0 0 18 75"><polyline points="1,0 16,37.5 1,75" fill="none" stroke="#e2e2e2" stroke-width="1"/></svg>

  <div class="abs strip-item strip-call">
    <span class="icon"><svg width="13" height="13" viewBox="0 0 24 24"><path fill="#fff" d="M6.6 10.8a15 15 0 0 0 6.6 6.6l2.2-2.2c.3-.3.7-.4 1-.2 1.1.4 2.3.6 3.6.6.6 0 1 .4 1 1V20c0 .6-.4 1-1 1C10.6 21 3 13.4 3 4c0-.6.4-1 1-1h3.5c.6 0 1 .4 1 1 0 1.3.2 2.5.6 3.6.1.3 0 .7-.2 1z"/></svg></span>
    <div><div class="strip-accent">Call to discuss</div><div class="strip-small">555.014.2870</div></div>
  </div>

  <div class="abs strip-item strip-place">
    <span class="icon"><svg width="12" height="14" viewBox="0 0 24 28"><path fill="#fff" d="M12 0a9 9 0 0 0-9 9c0 7 9 19 9 19s9-12 9-19a9 9 0 0 0-9-9zm0 13a4 4 0 1 1 0-8 4 4 0 0 1 0 8z"/></svg></span>
    <div class="strip-small">218 Orchard Lane<br>Suite 4<br>Fairhaven, Pa 19000</div>
  </div>

  <div class="abs strip-item strip-form">
    <span class="icon"><svg width="12" height="10" viewBox="0 0 12 10"><rect y="0" width="12" height="2" fill="#fff"/><rect y="4" width="12" height="2" fill="#fff"/><rect y="8" width="12" height="2" fill="#fff"/></svg></span>
    <div><div class="strip-small">Or Use our</div><div class="strip-accent">Contact form.</div></div>
  </div>
</section>

<section>
  <div class="abs bio"></div>
  <h1 class="abs bio-name">Daniel Marrow, PT, DPT, MS</h1>
  <p class="abs bio-text">Our services are the culmination of 15 years of experience of Dr. Daniel Marrow, PT, DPT, MS in the sports and orthopedic physical therapy arena. Daniel directed the rehabilitation services for the largest orthopedic group in Brook County. He has provided the services for an orthopedic and sports medicine group that had specialists in spine, shoulder, elbow, wrist, hand, hip, knee, ankle and foot surgery and treatment. His expertise is the treatment of any and all sports and orthopedic injuries, whether they are the result of trauma, repetitive movements or postures or the result of a surgical intervention. Daniel Marrow, PT, DPT, MS is confident that his extensive knowledge base and manual skills will drive Quillbrook Sports &amp; Orthopedic Physical Therapy to become a keystone in the private practice physical therapy community. Quillbrook is a direct extension of Daniel's dedication and commitment to become an integral health care provider in the community. Daniel relishes the fact that he is able to provide an atmosphere and facilities that are conducive towards a collective rehabilitation experience for clients that range from adolescents to geriatrics. Come in or correspond with our office. You will see that we value you as a client and would like to make you part of our community! If you have any questions about your injury and the treatment that you would receive, please contact us and you will be comforted in the fact that you have a partner in the community that you can trust.</p>
  <div class="abs bio-photo" role="img" aria-label="Portrait photo of the physical therapist in a light blue striped shirt"></div>
</section>

<section>
  <h2 class="abs services-title">Services</h2>
  <ul class="abs svc-list" style="left:112px;top:844px">
    <li>Sports Medicine rehabilitation</li><li>Orthopedic Injury rehabilitation</li><li>Post fracture rehabilitation</li>
    <li class="gap">Gait Analysis</li><li>Running Analysis</li>
  </ul>
  <ul class="abs svc-list" style="left:273px;top:844px">
    <li>Preoperative rehabilitation</li><li>Postoperative rehabilitation</li><li>Spine rehabilitation</li>
    <li class="gap">Worker's Compensation Injuries</li><li>Work Hardening</li><li>Motor Vehicle Injuries</li>
  </ul>
  <div class="abs svc-photo" role="img" aria-label="Photo of a therapist in an orange shirt treating a patient's back"></div>
  <ul class="abs svc-list" style="left:434px;top:844px">
    <li>ACL prehab (lower extremity injury prevention program)</li><li>Balance &amp; Proprioception training</li><li>Neurological rehabilitation</li><li>Hand and Upper extremity rehabilitation</li>
  </ul>
</section>

<section>
  <div class="abs testimonials"></div>
  <h2 class="abs testi-title">Testimonials</h2>
  <p class="abs testi-text">I would highly recommend Daniel to anyone who needs physical therapy. I went to Quillbrook for a minor running injury but I watched him work with other patients who were recovering from hip replacements, knee replacements, shoulder surgeries and various sports or work-related injuries. He is extremely knowledgeable and provides personalized care with compassion, professionalism and necessary doses of humor! After six weeks with Daniel, I was back to running again. I could not be happier with my experience!</p>
  <div class="abs testi-rule"></div>
  <div class="abs avatar" role="img" aria-label="Small portrait photo of the reviewer"></div>
  <div class="abs testi-who"><b>Marisa,</b> Place</div>
</section>

<footer>
  <div class="abs footer"></div>
  <div class="abs copyright">© Quillbrook Sports &amp; Orthopedic Physical Therapy</div>
  <span class="abs social" style="left:619px" aria-label="Social link"></span>
  <span class="abs social" style="left:657px" aria-label="Social link"></span>
</footer>

</body>
</html>
```